Business card for acupunctist in Melbourne. Specialises in Fertility, pre and post natal care, pain

I am looking for a business card which is going to catch people eyes. Two sided, one side in a muted colour (keeping it feminine) (pink or yellow???)maybe with a little simple logo or picture, the other side I was thinking white with 3 colours (pink grey and yellow... Had these in mind.
Info on the card
Marla Quenby Acupuncture

Dr Marla Quenby (TCM Acupuncture)
Acupuncture for balancing body and mind.
Fernleaf Wellcraft
14 Corran Lane, Elsworth 3071.
94726150
0438219574
Marlatcm@quenbymail.com

Some other little logo/ designs I have liked are as follows:
http://www.dorisfelkaclinic.com/rates-and-insurance/
http://www.corinnetavish.com/
http://www.rz-needlework.co.uk/

Target Market(s)

professional women, people in pain, active people, people seeking a healthy lifefstyle.

Industry/Entity Type

Business

Font styles to use
Serif
Sans Serif

Colors
eea4c8
fde08a
aaaaaa

Requirements
Must have
• Must be eye catching, but not too loud and busy. Subltle is good. Simple is also good. The logo could be something that represents growth and health and nurturing. Again not too elaborate, very simple.
Thankyou
Should not have
• Electric colours, crazy fonts, Pictures of yin and yang, candles, or bodies.

```html
<!DOCTYPE html>
<html lang="en">
<head>
<meta charset="utf-8">
<title>Marla Quenby Acupuncture – Business Card</title>
<link rel="stylesheet" href="https://fonts.googleapis.com/css2?family=Open+Sans:wght@400;600&family=Roboto+Condensed:wght@700&display=swap">
<style>
  :root {
    --page-bg: #f3f1f2;
    --magenta: #e0097f;
    --magenta-deep: #c8066f;
    --card-white: #f7f7f7;
    --lemon: #ebe20f;
    --ink: #1f1f1f;
    --grey-text: #6e6e6e;
    --white: #ffffff;
  }
  * { box-sizing: border-box; margin: 0; padding: 0; }
  html, body {
    width: 1200px;
    height: 1000px;
    overflow: hidden;
    background: var(--page-bg);
  }
  .canvas {
    position: relative;
    width: 1200px;
    height: 1000px;
  }
  .card {
    position: absolute;
    left: 250px;
    width: 700px;
    height: 400px;
    overflow: hidden;
    box-shadow: 0 6px 22px rgba(0,0,0,0.12);
  }
  .card svg { position: absolute; inset: 0; }

  /* Back of card */
  .card--back {
    top: 70px;
    background: var(--magenta);
  }
  .brand-mark {
    position: absolute;
    left: 150px;
    top: 150px;
    display: flex;
    align-items: center;
    gap: 14px;
    font-family: "Open Sans", sans-serif;
    font-weight: 400;
    font-size: 34px;
    letter-spacing: 0.02em;
    color: var(--white);
  }
  .brand-mark__dot {
    width: 14px;
    height: 14px;
    border-radius: 50%;
    background: var(--white);
  }

  /* Front of card */
  .card--front {
    top: 530px;
    background: var(--card-white);
  }
  .front-brand {
    position: absolute;
    left: 42px;
    top: 36px;
    font-family: "Open Sans", sans-serif;
    font-weight: 400;
    font-size: 17px;
    color: var(--ink);
  }
  .holder {
    position: absolute;
    left: 42px;
    top: 150px;
  }
  .holder__name {
    font-family: "Roboto Condensed", sans-serif;
    font-weight: 700;
    font-size: 30px;
    color: var(--ink);
    line-height: 1.1;
  }
  .holder__title {
    font-family: "Open Sans", sans-serif;
    font-size: 15px;
    color: var(--magenta);
    margin-top: 2px;
  }
  .contact {
    position: absolute;
    left: 42px;
    top: 245px;
    list-style: none;
    font-family: "Open Sans", sans-serif;
    font-size: 16px;
    line-height: 29px;
    letter-spacing: 0.04em;
    color: var(--grey-text);
  }
</style>
</head>
<body>
<main class="canvas">

  <section class="card card--back" aria-label="Card back">
    <svg width="700" height="400" viewBox="0 0 700 400" aria-hidden="true">
      <path class="back-stripe" d="M700 150 C610 175 545 225 540 300 L540 400" fill="none" stroke="#ffffff" stroke-width="9"/>
      <path class="back-stripe" d="M700 172 C630 195 572 240 568 310 L568 400" fill="none" stroke="#ffffff" stroke-width="9"/>
    </svg>
    <div class="brand-mark">
      <span>Marla Quenby Acupuncture</span>
      <span class="brand-mark__dot"></span>
    </div>
  </section>

  <section class="card card--front" aria-label="Card front">
    <svg width="700" height="400" viewBox="0 0 700 400" aria-hidden="true">
      <path class="front-lemon-band" d="M590 0 C485 12 455 150 425 260 C405 335 375 392 300 400" fill="none" stroke="#ebe20f" stroke-width="12"/>
      <path class="front-magenta-field" d="M614 0 C510 14 480 152 450 262 C430 336 400 392 328 400 L700 400 L700 0 Z" fill="#e0097f"/>
    </svg>
    <div class="front-brand">Marla Quenby Acupuncture</div>
    <div class="holder">
      <h1 class="holder__name">Dr Marla Quenby</h1>
      <p class="holder__title">(TCM Acupuncture)</p>
    </div>
    <ul class="contact">
      <li>94726150</li>
      <li>0438219574</li>
      <li>Marlatcm@quenbymail.com</li>
      <li>14 Corran Lane, Elsworth 3071</li>
    </ul>
  </section>

</main>
</body>
</html>
```